Insert card for anti-slip sticker

Product packaging should be inspired by the following
packaging and stand out at the same time: https://shopr.example/7QvKtwe

The packaging is not packaging in the conventional sense, but rather a kind of insert card that can be opened.
This can also be found in the linked product.

On the front of the card: Product name (20 anti-slip strips), advantages of the product and a appealing picture with the product

Inside: Instructions for use and product tips

Back: Images with possible uses, company headquarters, email for contact purposes, note about positive evaluation on Vendaro

```html
<!DOCTYPE html>
<html lang="de">
<head>
<meta charset="utf-8">
<title>Mara Lune – Anti-Rutsch Einlegekarte</title>
<link href="https://fonts.googleapis.com/css2?family=Source+Sans+3:wght@300;400;600&display=swap" rel="stylesheet">
<style>
:root{
  --ink:#1c1a18;
  --paper:#ffffff;
  --gold:#c98b4c;
  --gold-light:#e8c49a;
  --heading:#d08a3f;
  --text:#f2ede6;
  --dash:#ffffff;
}
*{margin:0;padding:0;box-sizing:border-box}
html,body{width:1005px;height:1200px;overflow:hidden;background:var(--paper)}
body{position:relative;font-family:"Source Sans 3",sans-serif;font-weight:300;color:var(--text)}
.panel{position:absolute;top:0;height:1200px;background:var(--ink)}
.panel--outside{left:0;width:480px}
.panel--inside{left:525px;width:480px}
.fold{position:absolute;top:0;height:1200px;border-left:1.5px dashed var(--dash)}
.fold--outside{left:240px}
.fold--inside{left:770px}
.abs{position:absolute}
.brand{color:var(--gold);font-weight:400;text-align:center;line-height:1}
.brand--back{left:0;width:240px;top:88px;font-size:40px}
.brand--front{left:240px;width:240px;top:168px;font-size:66px}
.brand-circle{left:324px;top:55px;width:84px;height:84px;border:1.5px solid var(--gold);border-radius:50%}
.photo{border:3px solid var(--gold)}
.use-photo{left:14px;width:212px;height:133px}
.use-label{left:0;width:240px;text-align:center;font-size:13.5px;letter-spacing:.3px}
.contact{left:0;width:240px;text-align:center;font-size:14px;line-height:21.3px}
.contact .gap{height:21px}
.web{font-weight:400;letter-spacing:.4px}
.hero-photo{left:254px;top:364px;width:212px;height:450px}
.count{left:254px;top:848px;font-size:70px;font-weight:400;color:var(--gold);line-height:1;letter-spacing:-2px}
.count-rule{left:339px;top:858px;height:56px;border-left:1.5px solid var(--text)}
.count-sub{left:350px;top:859px;font-size:19px;line-height:1}
.count-main{left:347px;top:884px;font-size:33px;font-weight:400;line-height:1;color:#fff}
.areas-pill{left:251px;top:946px;width:218px;height:20px;border:1px solid var(--text);border-radius:6px;font-size:10.5px;text-align:center;line-height:18px;letter-spacing:.3px}
.features{left:240px;width:240px;top:998px;text-align:center;font-size:13.5px;line-height:19px;letter-spacing:.2px}
.web--front{left:240px;width:240px;top:1114px;text-align:center;font-size:14px}
.heading{font-size:15.5px;font-weight:600;color:var(--heading);letter-spacing:.3px;line-height:1.35;text-transform:uppercase}
.copy{font-size:12.7px;line-height:21.2px}
.tips .heading,.tips .copy{left:549px;width:215px}
.aside .heading{left:797px;width:200px}
.aside .copy{left:797px;width:200px;font-size:10.6px;line-height:17.1px}
.aside .copy--install{font-size:11.4px;line-height:19px}
.circle{left:808px;width:164px;height:164px;border-radius:50%;border:3px solid var(--gold)}
.uses{left:797px;top:250px;display:grid;grid-template-columns:88px 112px;font-size:11.5px;line-height:19.2px}
.uses li{list-style:none}
.uses li::before{content:"• ";font-size:9px}
</style>
</head>
<body>
<section class="panel panel--outside">
  <div class="abs brand brand--back">Mara<br>Lune</div>

  <div class="abs photo use-photo" style="top:234px;background:linear-gradient(180deg,#e6e6e4 0%,#fafafa 55%,#d9d9d7 100%)" role="img" aria-label="Weiße Badewanne mit Chromarmatur"></div>
  <p class="abs use-label" style="top:375px">BAD</p>
  <div class="abs photo use-photo" style="top:415px;background:linear-gradient(135deg,#4a4a4e 0%,#6a6a70 60%,#55555a 100%)" role="img" aria-label="Handbrause mit fließendem Wasser vor grauen Fliesen"></div>
  <p class="abs use-label" style="top:555px">DUSCHE</p>
  <div class="abs photo use-photo" style="top:596px;background:linear-gradient(180deg,#8fb8ac 0%,#7fa79c 45%,#5a6262 60%,#e8e8e8 85%)" role="img" aria-label="Waschbecken mit Armatur vor mintgrüner Wand"></div>
  <p class="abs use-label" style="top:735px">WANNE</p>
  <div class="abs photo use-photo" style="top:776px;background:linear-gradient(135deg,#51606c 0%,#8a98a4 50%,#5a6874 100%)" role="img" aria-label="Fuß auf nasser Fläche mit Wassertropfen"></div>
  <p class="abs use-label" style="top:916px">NASSBEREICH</p>

  <div class="abs contact" style="top:980px">
    <p>Contact Information</p>
    <p>Adress:</p>
    <p>Lorem ipsum</p>
    <p>Lorem ipsum</p>
    <div class="gap"></div>
    <p>Lorem ipsum</p>
    <p>Lorem ipsum</p>
    <p class="web" style="margin-top:12px">www.maralune.example</p>
  </div>

  <div class="abs brand-circle"></div>
  <div class="abs brand brand--front">Mara<br>Lune</div>
  <div class="abs photo hero-photo" style="background:linear-gradient(180deg,#111 0%,#2a2420 40%,#1a1a1c 75%,#333 100%)" role="img" aria-label="Nasse Beine auf dunklem Boden mit transparenten Anti-Rutsch-Streifen"></div>

  <div class="abs count">20</div>
  <div class="abs count-rule"></div>
  <div class="abs count-sub">Anti-Rutsch</div>
  <div class="abs count-main">Streifen</div>
  <div class="abs areas-pill">BAD / DUSCHE / WANNE / NASSBEREICH</div>
  <div class="abs features">
    <p>PREMIUM QUALITAT</p>
    <p>ELEGANT UND KAUM SICHTBAR</p>
    <p>EXTREM STARKER HALT</p>
    <p>ABSTANDSHALTER enthalten</p>
  </div>
  <p class="abs web web--front">www.maralune.example</p>
</section>
<div class="fold fold--outside"></div>

<section class="panel panel--inside"></section>
<div class="fold fold--inside"></div>

<div class="tips">
  <h2 class="abs heading" style="top:66px">Mehr Sicherheit im Bad</h2>
  <p class="abs copy" style="top:94px">Gerade in der Badewannen oder Dusche, wo man mit eingeseiften Füßen schnell den Halt verliert, ist Handlungsbedarf! Wir bieten Ihnen mit unseren Anti Rutsch Streifen geprüften Rutschschutz.</p>

  <h2 class="abs heading" style="top:278px">100% Rustscfest</h2>
  <p class="abs copy" style="top:308px">Ob Treppenstufen oder im Badezimmer unsere Anti-Rutsch-Aufkleberbieten Rutschfesten Halt. Verzichten Sie auf eine Dusch oder Badewanneneinlage. Die Antirutschstreifen bietenIhnen sicheren Halt.</p>

  <h2 class="abs heading" style="top:524px">Hygienischer &amp; Sauber</h2>
  <p class="abs copy" style="top:553px;width:220px">Anti-Rutsch Aufkleber sind effektiver &amp; hygienischer als eine Badewannenmatte oder Duscheinlage. Rutsch-Schutz Sticker als ideale Lösung gegen Schmutz &amp; Schimmel in der Wanne oder Dusche.</p>

  <h2 class="abs heading" style="top:737px">Universell einsetzbar</h2>
  <p class="abs copy" style="top:766px">Die Antirutsch Aufkleber sind transparent,extra dünn und so gut wie unsichtbar! Ob als Rutschmatte Badewanne oder als Rutschstreifen für Treppen. Einfach zu Kleben und 100% Rutschfest</p>

  <h2 class="abs heading" style="top:949px">Premium Rustschutz</h2>
  <p class="abs copy" style="top:980px">Ein tolles Geschenk für jeden Anlass, hiermit ersetzen Sie die normale Antirutschmatte oder Duschmatte. Verabschieden Sie sich von rutschigen Stufen, Fliesen, Treppe oder der Duschwanne im Bad.</p>
</div>

<div class="aside">
  <div class="abs circle" style="top:43px;background:linear-gradient(180deg,#8a8c8e 0%,#e9e9e7 40%,#f4f4f2 100%)" role="img" aria-label="Duschwanne mit aufgeklebten Streifen und Packung mit 20 Streifen"></div>
  <h2 class="abs heading" style="top:225px">Anwendungsbereich</h2>
  <ul class="abs uses">
    <li>Fliesen</li><li>Bodenfliesen</li>
    <li>Duschen</li><li>Fußmatten</li>
    <li>Badewannen</li><li>Pool &amp; Nassbereich</li>
  </ul>

  <div class="abs circle" style="top:352px;background:linear-gradient(135deg,#c9a170 0%,#e4c9a2 50%,#b58c5c 100%)" role="img" aria-label="Kleinkind auf einer Holztreppe"></div>
  <h2 class="abs heading" style="top:532px">Sicherheit geht vor</h2>
  <p class="abs copy" style="top:560px">Ihr Bad wird rutschsicher! Mit unseren Antirutsch Aufklebern von Mara Lune. Ihr Badendlich auch ohne lose Duschmatte mit Ablagerungen unfallsicher! Sie erwerben ein zeitlos ansprechendes Anti Rutsch System welches 2019 überarbe-itet wurde und für noch mehr Komfort in Ihrem Badezimmer sorgt</p>

  <div class="abs circle" style="top:747px;background:linear-gradient(135deg,#1c1c1c 0%,#8c8c8c 35%,#202020 50%,#9a9a9a 70%,#1c1c1c 100%)" role="img" aria-label="Nahaufnahme der strukturierten Anti-Rutsch-Streifen"></div>
  <h2 class="abs heading" style="top:930px">Kinderleichte<br>Installation</h2>
  <p class="abs copy copy--install" style="top:986px">Mit der selbstklebenden Rückseite werden die Anti-Rutsch-Aufkleber verklebt. Sollten Sie Lust auf ein neues Muster haben, ist esmöglich trotz starker Klebekraft unsere Aufkleber Rückstandslos zu entfer-nen. Sollten Sie Fragen haben, stehen wir Ihnen jederzeit zur Verfügung</p>
</div>
</body>
</html>
```